I need a general brochure for a new non-profit committed to empowering survivors of sexual exploitation. I kept the wording to a minimum so the design will help me tell the story. The brochure will be used in churches and other venues when I give presentations. I will also be using this in one on one presentations to walk through the highlights of our work. We are in the aftercare business and the feel should communicate hope and new beginnings.

I would like a single fold brochure- about 8.5x5.5.
Updates

to clarify- the brochure should be 8.5 by 5.5 Added Wednesday, November 05, 2014

Target Market(s)

donors, volunteers- all ages- mainly women

Industry/Entity Type

Non-Profit

Font styles to use
Serif

Requirements
Must have
• Pictures draw me in. I tend to like professional designs with just enough color and detail to make them unique.
• Hopeful- note the picture I attached are bright- not sad and depressed. Feel free to add your own photos if they are better. My favorite picture is the black woman with sun.
• Please use a variety of races- we serve a diverse population.
• I also need my website listed www.brightmorrowhaven.org
Nice to have
• I have seen some designs that use one picture to stretch across the front and back of the brochure. This might be interesting if it works, but I may have too much text on the back to make this worthwhile.
Should not have
• hearts, country feel, goofy, whimsical

```html
<!DOCTYPE html>
<html lang="en">
<head>
<meta charset="utf-8">
<title>Bright Morrow Haven – Brochure Spread</title>
<link rel="stylesheet" href="https://fonts.googleapis.com/css2?family=Encode+Sans+Semi+Condensed:wght@300;400&family=PT+Sans+Narrow:wght@400;700&display=swap">
<style>
  :root{
    --gold:#f5c400;
    --royal:#1f48b4;
    --navy:#17307a;
    --ink:#1d3a8f;
    --panel:rgba(232,238,250,0.86);
    --veil:rgba(22,44,110,0.55);
    --white:#ffffff;
  }
  *{margin:0;padding:0;box-sizing:border-box}
  html,body{width:1200px;height:389px;overflow:hidden;background:#fff}
  .spread{position:relative;width:1200px;height:389px;overflow:hidden;font-family:"PT Sans Narrow",Arial,sans-serif}
  h2,h3{font-weight:400}
  .photo{position:absolute;top:0;height:389px}
  .photo--study{left:0;width:610px;background:linear-gradient(100deg,#6b4a36 0%,#a67c5b 28%,#d9c3a8 45%,#8b6a55 62%,#4c3a33 100%)}
  .photo--friends{left:600px;width:600px;background:linear-gradient(90deg,#3a3330 0%,#6e5447 25%,#a27a63 45%,#c79b82 60%,#7a6d78 78%,#2c56b8 100%)}
  .veil{position:absolute;left:0;top:0;width:420px;height:176px;background:var(--veil)}
  .band-gold{position:absolute;left:760px;top:0;width:440px;height:9px;background:var(--gold)}
  .band-blue{position:absolute;left:1130px;top:9px;width:70px;height:380px;background:var(--royal)}

  .statement{position:absolute;left:22px;color:var(--white)}
  .statement h2{font-family:"Encode Sans Semi Condensed",Arial,sans-serif;font-weight:400;font-size:25px;color:var(--gold);line-height:1}
  .statement p{font-size:12px;line-height:1.35;margin-top:6px}
  .statement--vision{top:26px}
  .statement--vision p{width:190px}
  .statement--mission{top:95px}
  .statement--mission p{width:200px}
  .bullet{position:absolute;width:18px;height:1px;background:var(--gold)}
  .bullet::after{content:"";position:absolute;right:-3px;top:-2px;width:5px;height:5px;border-radius:50%;background:var(--gold)}

  .model-rule{position:absolute;left:420px;top:0;width:1.5px;height:389px;background:var(--gold)}
  .model-title{position:absolute;left:401px;top:160px;transform:rotate(-90deg);transform-origin:left top;font-family:"Encode Sans Semi Condensed",Arial,sans-serif;font-weight:400;font-size:25px;color:var(--gold);white-space:nowrap}

  .card{position:absolute;background:var(--panel);color:var(--ink);border:1px solid rgba(255,255,255,0.7);overflow:hidden}
  .card h3{font-family:"Encode Sans Semi Condensed",Arial,sans-serif;font-weight:300;line-height:1;color:var(--navy)}
  .card p{font-size:11px;line-height:1.25;margin-top:3px}
  .step{left:434px;width:144px;padding:5px 6px}
  .step h3{font-size:26px}
  .step--heal{top:12px;height:160px}
  .step--discover{top:177px;height:95px}
  .step--overcome{top:279px;height:94px}

  .role{text-align:right;padding:6px 8px}
  .role h3{font-size:27px}
  .role--mentor{left:772px;top:30px;width:428px;height:110px}
  .role--mentor p{margin-left:auto;width:250px}
  .role--teacher{left:1060px;top:150px;width:140px;height:138px}
  .role--partner{left:815px;top:296px;width:226px;height:68px;text-align:center}
  .role--supporter{left:1030px;top:296px;width:170px;height:68px}

  .role-title{position:absolute;left:645px;top:334px;font-family:"Encode Sans Semi Condensed",Arial,sans-serif;font-weight:400;font-size:25px;color:var(--gold)}
  .role-rule{position:absolute;left:630px;top:372px;width:555px;height:1.5px;background:var(--gold)}
  .role-rule::after{content:"";position:absolute;right:-4px;top:-3px;width:7px;height:7px;border-radius:50%;background:var(--gold)}
  .role-dot{position:absolute;left:632px;top:349px;width:6px;height:6px;border-radius:50%;background:var(--gold)}
</style>
</head>
<body>
<main class="spread">
  <div class="photo photo--study" role="img" aria-label="Photo of a young woman with glasses studying at a desk beside a stack of books in a library"></div>
  <div class="photo photo--friends" role="img" aria-label="Photo of two smiling young women posing close together"></div>
  <div class="veil"></div>
  <div class="band-gold"></div>
  <div class="band-blue"></div>

  <section class="statement statement--vision">
    <span class="bullet" style="left:-22px;top:12px"></span>
    <h2>Vision</h2>
    <p>Survivors of sexual exploitation live free, fulfilling their God-given purpose.</p>
  </section>
  <section class="statement statement--mission">
    <span class="bullet" style="left:-22px;top:12px"></span>
    <h2>Mission</h2>
    <p>Mobilize communities to encourage and equip survivors of sexual exploitation to build new lives.</p>
  </section>

  <div class="model-rule"></div>
  <h2 class="model-title">Our Model</h2>

  <article class="card step step--heal">
    <h3>Heal</h3>
    <p>Survivors need safe relationships and a safe environment to heal. Bright Morrow Haven facilitates mentor relationships, offers a supportive community and immerses survivors in faith-based curriculum.</p>
  </article>
  <article class="card step step--discover">
    <h3>Discover</h3>
    <p>In order to thrive, survivors need to discover their innate ability, preferences, personality and spiritual gifts.</p>
  </article>
  <article class="card step step--overcome">
    <h3>Overcome</h3>
    <p>Survivors overcome barriers to moving ahead with the right educational and employment options.</p>
  </article>

  <article class="card role role--mentor">
    <h3>Mentor</h3>
    <p>Build a safe nurturing relationship with one woman and encourage her to reach her goals. Join a community who receive training and support to effectively mentor.</p>
  </article>
  <article class="card role role--teacher">
    <h3>Teacher</h3>
    <p>Teach group classes on life skills, biblical studies, physical wellbeing, creative arts, conflict resolution, emotional health, literacy, and financial management.</p>
  </article>
  <article class="card role role--partner">
    <h3>Business Partner</h3>
    <p>Provide employment and business coaching to a survivor.</p>
  </article>
  <article class="card role role--supporter">
    <h3>Supporter</h3>
    <p>Financially and prayerfully support the work of Bright Morrow Haven.</p>
  </article>

  <span class="role-dot"></span>
  <h2 class="role-title">Your Role</h2>
  <div class="role-rule"></div>
</main>
</body>
</html>
```